we are plumbers and builders.

one side with kestrel fittings mark henley 07812345670 01632960418 info@kestrelfittings.co.uk
other side
kestrel building
dean henley 07700900314
01632960418
info@kestrelbuilding.co.uk

i don't want your bog standard logo id like something unusual maybe shape the card. i like black and silver,

```html
<!DOCTYPE html>
<html lang="en">
<head>
<meta charset="utf-8">
<title>Kestrel business cards</title>
<link rel="stylesheet" href="https://fonts.googleapis.com/css2?family=Montserrat:wght@400;500;700&display=swap">
<style>
  :root {
    --backdrop: #e3e3e3;
    --card-dark: #2a2a2a;
    --card-light: #f4f4f4;
    --brand-red: #e0202a;
    --icon-blue: #4a72c4;
    --silver: #a9a9a9;
    --divider-dark: #6a6a6a;
    --divider-light: #b5b5b5;
    --ink-light: #ffffff;
    --ink-dark: #262626;
  }
  * { margin: 0; padding: 0; box-sizing: border-box; }
  html, body {
    width: 1200px;
    height: 960px;
    overflow: hidden;
    background: var(--backdrop);
    font-family: "Montserrat", Arial, sans-serif;
  }
  .card {
    position: absolute;
    left: 327px;
    width: 550px;
    height: 356px;
  }
  .card--fittings { top: 108px; background: var(--card-dark); color: var(--ink-light); }
  .card--building { top: 496px; background: var(--card-light); color: var(--ink-dark); }

  .brand {
    position: absolute;
    left: 33px;
    top: 147px;
    display: flex;
    align-items: center;
    gap: 14px;
  }
  .brand__circle {
    width: 58px;
    height: 58px;
    border-radius: 50%;
    border: 5px solid var(--silver);
  }
  .brand__name {
    color: var(--brand-red);
    font-weight: 500;
    font-size: 24px;
    line-height: 27px;
    letter-spacing: 1px;
    text-transform: uppercase;
  }

  .divider {
    position: absolute;
    left: 274px;
    top: 112px;
    width: 2px;
    height: 132px;
  }
  .card--fittings .divider { background: var(--divider-dark); }
  .card--building .divider { background: var(--divider-light); }

  .contact {
    position: absolute;
    left: 290px;
    top: 109px;
  }
  .contact__name {
    color: var(--brand-red);
    font-weight: 700;
    font-size: 19px;
    line-height: 22px;
    text-transform: uppercase;
  }
  .contact__role {
    font-size: 15px;
    line-height: 20px;
    margin-bottom: 17px;
  }
  .contact__list { list-style: none; }
  .contact__item {
    display: flex;
    align-items: center;
    gap: 4px;
    font-size: 15px;
    line-height: 19.3px;
  }
  .contact__icon {
    width: 14px;
    height: 14px;
    flex: none;
    fill: none;
    stroke: var(--icon-blue);
    stroke-width: 1.4;
  }
  .contact__icon--solid { fill: var(--icon-blue); stroke: none; }
</style>
</head>
<body>

<section class="card card--fittings">
  <div class="brand">
    <span class="brand__circle"></span>
    <span class="brand__name">Kestrel<br>Fittings</span>
  </div>
  <span class="divider"></span>
  <div class="contact">
    <p class="contact__name">Mark Henley</p>
    <p class="contact__role">Owner</p>
    <ul class="contact__list">
      <li class="contact__item">
        <svg class="contact__icon" viewBox="0 0 14 14"><rect x="3.5" y="1" width="7" height="12" rx="1"/><line x1="6" y1="11" x2="8" y2="11"/></svg>
        07812345670
      </li>
      <li class="contact__item">
        <svg class="contact__icon contact__icon--solid" viewBox="0 0 14 14"><path d="M3 1l2.5 2.8-1.3 1.7c.8 1.8 2.2 3.2 4 4l1.7-1.3L12.7 11 11 13C6 12.6 1.4 8 1 3z"/></svg>
        01632960418
      </li>
      <li class="contact__item">
        <svg class="contact__icon" viewBox="0 0 14 14"><rect x="1" y="3" width="12" height="8.5"/><path d="M1 3l6 5 6-5"/></svg>
        info@kestrelfittings.co.uk
      </li>
      <li class="contact__item">
        <svg class="contact__icon" viewBox="0 0 14 14"><circle cx="7" cy="7" r="5.8"/><ellipse cx="7" cy="7" rx="2.5" ry="5.8"/><line x1="1.2" y1="7" x2="12.8" y2="7"/></svg>
        www.kestrelfittings.co.uk
      </li>
    </ul>
  </div>
</section>

<section class="card card--building">
  <div class="brand">
    <span class="brand__circle"></span>
    <span class="brand__name">Kestrel<br>Building</span>
  </div>
  <span class="divider"></span>
  <div class="contact">
    <p class="contact__name">Dean Henley</p>
    <p class="contact__role">Owner</p>
    <ul class="contact__list">
      <li class="contact__item">
        <svg class="contact__icon" viewBox="0 0 14 14"><rect x="3.5" y="1" width="7" height="12" rx="1"/><line x1="6" y1="11" x2="8" y2="11"/></svg>
        07700900314
      </li>
      <li class="contact__item">
        <svg class="contact__icon contact__icon--solid" viewBox="0 0 14 14"><path d="M3 1l2.5 2.8-1.3 1.7c.8 1.8 2.2 3.2 4 4l1.7-1.3L12.7 11 11 13C6 12.6 1.4 8 1 3z"/></svg>
        01632960418
      </li>
      <li class="contact__item">
        <svg class="contact__icon" viewBox="0 0 14 14"><rect x="1" y="3" width="12" height="8.5"/><path d="M1 3l6 5 6-5"/></svg>
        info@kestrelbuilding.co.uk
      </li>
      <li class="contact__item">
        <svg class="contact__icon" viewBox="0 0 14 14"><circle cx="7" cy="7" r="5.8"/><ellipse cx="7" cy="7" rx="2.5" ry="5.8"/><line x1="1.2" y1="7" x2="12.8" y2="7"/></svg>
        www.kestrelbuilding.co.uk
      </li>
    </ul>
  </div>
</section>

</body>
</html>
```